Perfect — here’s the updated version of your description with **title #1** and the integration/booking functionality references removed, while still keeping the “motivation to book” idea in the design style:
---
**Luxury Property Website Design – Dominican Republic**
We are looking to create a professional and visually appealing **website design** for a premium property that we will be promoting as a short-term rental.
The property is located in an **exclusive area of the Dominican Republic** and offers a high-end experience for guests. Our goal is to create a website that highlights the **luxury, comfort, and exclusivity** of the property, while motivating visitors to **make a reservation inquiry**.
**Key Requirements:**
* A clean, modern, and elegant design that reflects the **premium nature** of the property.
* High-quality visual presentation of the **property’s best features** (rooms, amenities, location, views, nearby attractions).
* Easy-to-navigate structure
* Mobile-friendly and optimized for all screen sizes.
* Space for testimonials or guest reviews to build trust.
**Design Style We Like:**
* Elegant and sophisticated, with a touch of tropical luxury.
* Use of high-quality photography, subtle animations, and a warm color palette that reflects the Caribbean atmosphere.
* A premium feel, similar to boutique hotel or luxury villa rental websites.
**Deliverables:**
* Homepage design.
* Property detail page design (with gallery, amenities, and booking inquiry section).
Contact page or About Us page
* Photo Gallery
The final design should capture the essence of a **luxury getaway** and make visitors feel compelled to reserve their night.

```html
<!DOCTYPE html>
<html lang="en">
<head>
<meta charset="utf-8">
<title>Casa Coralina – Luxury Villas</title>
<link href="https://fonts.googleapis.com/css2?family=Marcellus&family=Poppins:wght@400;500;600&display=swap" rel="stylesheet">
<style>
:root{
  --navy:#1c2659;
  --navy-deep:#161f4d;
  --gold:#c9a02a;
  --gold-soft:#e9d9a8;
  --ink:#1f2433;
  --muted:#6b6f7c;
  --white:#ffffff;
  --serif:'Marcellus', Georgia, serif;
  --sans:'Poppins', Arial, sans-serif;
}
*{box-sizing:border-box;margin:0;padding:0}
html,body{width:1200px;height:4605px;overflow:hidden}
body{position:relative;background:var(--white);font-family:var(--sans);color:var(--ink)}
.abs{position:absolute}
.photo{position:absolute;display:block}
.serif{font-family:var(--serif);font-weight:400}

/* hero */
.hero{position:absolute;left:0;top:0;width:1200px;height:733px;
  background:linear-gradient(180deg,#6f8a5c 0%,#a89a78 30%,#7f6e55 55%,#4f5f3a 78%,#3c4a2c 100%)}
.nav{position:absolute;left:63px;top:30px;width:1076px;height:59px;background:var(--white);
  display:flex;align-items:center;padding:0 16px 0 16px}
.brand{font-family:var(--sans);font-weight:500;font-size:25px;color:var(--navy)}
.nav-links{display:flex;gap:29px;margin-left:auto;margin-right:44px;font-size:13px;color:var(--ink)}
.btn{display:inline-flex;align-items:center;justify-content:center;font-family:var(--sans);
  font-weight:600;font-size:12px;letter-spacing:.3px;text-transform:uppercase;border-radius:4px}
.btn-navy{background:var(--navy);color:var(--white)}
.btn-gold{background:var(--gold);color:var(--white)}
.btn-white{background:var(--white);color:var(--navy)}
.hero-title{left:61px;top:478px;font-family:var(--serif);font-size:62px;line-height:72px;color:var(--white)}
.hero-card{left:776px;top:474px;width:363px;height:137px;background:var(--white);border-radius:6px;padding:8px}
.hero-card .photo{left:8px;top:8px;width:150px;height:121px;background:linear-gradient(180deg,#7ea8d6,#9c9f92 60%,#3f6aa0);border-radius:4px}
.hero-card .num{position:absolute;left:174px;top:14px;font-family:var(--serif);font-size:40px;color:var(--navy)}
.hero-card .txt{position:absolute;left:174px;top:56px;font-size:18px;line-height:21px;color:var(--navy)}
.hero-card .more{position:absolute;left:174px;top:102px;font-size:10px;font-weight:600;color:var(--navy);text-decoration:underline}
.review{left:775px;top:626px;width:365px;height:73px;border:1px solid rgba(255,255,255,.6);border-radius:6px;
  background:rgba(255,255,255,.18);display:flex;align-items:center;padding:0 10px;color:var(--white)}
.avatars{display:flex}
.avatars span{width:48px;height:48px;border-radius:50%;border:2px solid var(--white);background:#9aa0b3;margin-right:-12px}
.review .score{margin-left:26px;font-family:var(--serif);font-size:34px}
.review .star{color:var(--gold);font-size:26px;margin-left:4px}
.review .lbl{margin-left:14px;font-size:13px;font-weight:600;line-height:18px}

/* section labels */
.eyebrow{position:absolute;left:0;width:1200px;text-align:center;font-family:var(--serif);font-size:22px;color:var(--gold)}
.eyebrow::before,.eyebrow::after{content:"";display:inline-block;width:58px;height:1px;background:var(--gold);vertical-align:middle;margin:0 10px}
.section-title{position:absolute;left:0;width:1200px;text-align:center;font-family:var(--serif);font-weight:400;font-size:46px;color:var(--navy)}

/* about */
.about-text{left:704px;width:440px}
.about-text .kicker{font-family:var(--serif);font-size:22px;color:var(--gold)}
.about-text .kicker::after{content:"";display:inline-block;width:52px;height:1px;background:var(--gold);vertical-align:middle;margin-left:8px}
.about-text h2{font-family:var(--serif);font-weight:400;font-size:47px;line-height:54px;color:var(--navy);margin-top:8px}
.about-text p{font-size:12.5px;line-height:21px;color:var(--muted);margin-top:18px;width:400px}
.stats{display:flex;margin-top:26px}
.stat{padding-right:28px;margin-right:28px;border-right:1px solid #c9cbd4}
.stat:last-child{border:0;margin:0;padding:0}
.stat b{display:block;font-family:var(--serif);font-weight:400;font-size:40px;color:var(--navy);line-height:46px}
.stat span{font-size:13px;color:var(--muted)}

/* property cards */
.prop{position:absolute;top:1507px;width:347px;height:472px;background:var(--white)}
.prop.raised{box-shadow:0 6px 24px rgba(20,30,70,.12)}
.prop .photo{left:0;top:0;width:347px;height:229px}
.tag{position:absolute;left:19px;top:20px;background:var(--white);font-size:12px;padding:4px 9px;border-radius:3px}
.prop h3{position:absolute;left:22px;top:250px;font-family:var(--serif);font-weight:400;font-size:23px;color:var(--navy)}
.prop .loc{position:absolute;left:22px;top:284px;font-size:13px;color:var(--muted);display:flex;align-items:center;gap:6px}
.prop .desc{position:absolute;left:22px;top:314px;width:310px;font-size:11px;line-height:19px;color:var(--muted)}
.feats{position:absolute;left:22px;top:370px;display:flex;align-items:center;font-size:11px;color:var(--muted)}
.feats span{display:flex;align-items:center;gap:6px}
.feats i{width:1px;height:20px;background:#c9cbd4;margin:0 18px}
.prop .btn{position:absolute;left:22px;top:411px;width:170px;height:37px}
.dots{position:absolute;left:0;width:1200px;display:flex;justify-content:center;gap:4px}
.dots span{width:10px;height:10px;border-radius:50%;background:#d5d6dc}
.dots span.on{background:var(--gold)}

/* facilities */
.facilities{position:absolute;left:0;top:2124px;width:1200px;height:504px;
  background:linear-gradient(180deg,#2a3a78 0%,#34477f 45%,#22305f 75%,#1d2a58 100%)}
.facilities .eyebrow{top:98px}
.facilities .section-title{top:140px;color:var(--white)}
.fac{position:absolute;top:214px;width:256px;height:199px;background:var(--white);border-radius:3px;text-align:center}
.fac .ico{position:absolute;left:94px;top:26px;width:66px;height:60px;border-radius:50%;background:var(--gold-soft)}
.fac h4{position:absolute;left:0;top:116px;width:100%;font-family:var(--sans);font-weight:500;font-size:20px;color:var(--navy)}
.fac p{position:absolute;left:18px;top:148px;width:220px;font-size:11.5px;line-height:19px;color:var(--muted)}
.arrow{position:absolute;width:22px;height:32px}

/* testimonials */
.testi{position:absolute;top:3407px;width:347px;height:378px;background:var(--white);box-shadow:0 4px 22px rgba(20,30,70,.09);text-align:center}
.stars{position:absolute;left:0;top:44px;width:100%;color:var(--gold);font-size:26px;letter-spacing:3px}
.testi p{position:absolute;left:26px;top:85px;width:295px;font-size:12.5px;line-height:21px;color:var(--ink)}
.testi .face{position:absolute;left:138px;top:204px;width:70px;height:70px;border-radius:50%;background:#b7b2ad}
.testi h5{position:absolute;left:0;top:290px;width:100%;font-family:var(--sans);font-weight:500;font-size:20px;color:var(--navy)}
.testi .date{position:absolute;left:0;top:320px;width:100%;font-size:13px;color:var(--ink)}
.testi .quote{position:absolute;right:20px;top:300px;font-family:var(--serif);font-size:96px;line-height:96px;color:var(--gold-soft)}

/* signup + footer */
.dark{position:absolute;left:0;top:3928px;width:1200px;height:677px;background:var(--navy-deep)}
.dark h2{position:absolute;left:0;top:82px;width:1200px;text-align:center;font-family:var(--serif);font-weight:400;font-size:50px;color:var(--white)}
.dark .lead{position:absolute;left:260px;top:160px;width:680px;text-align:center;font-size:13px;line-height:23px;color:#d9dbe6}
.signup{position:absolute;left:282px;top:223px;width:660px;height:57px;border:1px solid #c9cbd8;border-radius:4px;display:flex;align-items:center;padding:0 4px 0 22px}
.signup span{font-size:13px;color:#e3e5ee}
.signup .btn{margin-left:auto;width:172px;height:45px;font-size:13px}
.foot-brand{position:absolute;left:57px;top:373px;font-family:var(--sans);font-weight:500;font-size:27px;color:var(--white)}
.foot-about{position:absolute;left:57px;top:422px;width:320px;font-size:12px;line-height:19px;color:#d0d3e0}
.socials{position:absolute;left:57px;top:526px;display:flex;gap:10px}
.socials span{width:29px;height:29px;border:1.5px solid var(--white);border-radius:50%}
.col h6{font-family:var(--sans);font-weight:600;font-size:15px;color:var(--white);text-transform:uppercase;margin-bottom:14px}
.col li{list-style:none;font-size:12.5px;line-height:25px;color:#e0e2ea}
.contact li{display:flex;align-items:center;gap:12px;line-height:29px}
.thumb{position:absolute;width:108px;height:71px}
.rule{position:absolute;left:0;top:613px;width:1200px;height:1px;background:#3c4578}
.copy{position:absolute;left:0;top:638px;width:1200px;text-align:center;font-size:12px;color:#d0d3e0}
</style>
</head>
<body>

<section class="hero">
  <div class="photo" role="img" aria-label="Modern two-storey luxury villa with pool and tropical lawn at dusk" style="inset:0;background:linear-gradient(180deg,rgba(120,150,110,.6),rgba(140,120,90,.2) 40%,rgba(40,50,30,.35))"></div>
  <nav class="nav">
    <div class="brand">Casa Coralina</div>
    <div class="nav-links"><span>Home</span><span>About Us</span><span>Property</span><span>Gallery</span><span>Contact Us</span></div>
    <a class="btn btn-navy" style="width:132px;height:37px">Book Now</a>
  </nav>
  <h1 class="abs hero-title serif">Luxury Properties That<br>Match Your Lifestyle.</h1>
  <a class="abs btn btn-white" style="left:61px;top:647px;width:182px;height:38px">Explore The Villa</a>
  <div class="abs hero-card">
    <div class="photo" role="img" aria-label="Villa exterior with pool"></div>
    <div class="num">250+</div>
    <div class="txt">Luxury Properties<br>For Sale...</div>
    <div class="more">EXPLORE NOW →</div>
  </div>
  <div class="abs review">
    <div class="avatars" role="img" aria-label="Customer portraits"><span></span><span></span><span></span></div>
    <div class="score">4.9</div><div class="star">★</div>
    <div class="lbl">Reviewed By 12k+<br>Happy Customers</div>
  </div>
</section>

<div class="photo" role="img" aria-label="Lush garden with turquoise pool" style="left:61px;top:890px;width:264px;height:394px;background:linear-gradient(180deg,#4f6a3c 0%,#6e8b55 45%,#5fb6b7 70%,#3f9aa0 100%)"></div>
<div class="photo" role="img" aria-label="Stone terrace with wall lights and potted palm" style="left:340px;top:822px;width:316px;height:462px;background:linear-gradient(160deg,#6a5b4a 0%,#b9ab98 35%,#d8ccb9 65%,#9f8d74 100%)"></div>
<div class="abs about-text" style="top:847px">
  <div class="kicker">About Us</div>
  <h2>The Dominican<br>Republic, Redefined</h2>
  <p>Lorem Ipsum Is Simply Dummy Text Of The Printing And Typesetting Industry. Lorem Ipsum Has Been The Industry's Standard Dummy Text Ever Since The 1500s, When An Unknown Printer Took A Galley..</p>
  <div class="stats">
    <div class="stat"><b>250+</b><span>Luxury Villas</span></div>
    <div class="stat"><b>★ 4.9</b><span>Guest Rating</span></div>
    <div class="stat"><b>12k+</b><span>Happy Customers</span></div>
  </div>
  <a class="btn btn-gold" style="margin-top:24px;width:212px;height:40px">Learn More About Us</a>
</div>

<div class="eyebrow" style="top:1376px">Properties</div>
<h2 class="section-title" style="top:1411px">Featured Properties</h2>

<article class="prop" style="left:61px">
  <div class="photo" role="img" aria-label="White modern villa on green lawn" style="background:linear-gradient(180deg,#8fb3d9,#c5c8c0 55%,#5f8a4c)"></div>
  <span class="tag">For Sale</span>
  <h3>Luxury Villa Property</h3>
  <div class="loc"><svg width="10" height="13" viewBox="0 0 10 13"><path d="M5 0a5 5 0 0 0-5 5c0 3.5 5 8 5 8s5-4.5 5-8a5 5 0 0 0-5-5zm0 7a2 2 0 1 1 0-4 2 2 0 0 1 0 4z" fill="#1c2659"/></svg>Dominican Republic</div>
  <div class="desc">It Has Survived Not Only Five Centuries, But Also The Leap Into Sed Electronic Typesetting, Remaining.</div>
  <div class="feats"><span><svg width="18" height="11" viewBox="0 0 18 11"><path d="M1 0v11M1 7h16v4M4 4h13v3" stroke="#1c2659" stroke-width="1.6" fill="none"/></svg>8 BED</span><i></i><span><svg width="14" height="13" viewBox="0 0 14 13"><path d="M1 6h12v3a3 3 0 0 1-3 3H4a3 3 0 0 1-3-3zM3 6V1h3" stroke="#1c2659" stroke-width="1.5" fill="none"/></svg>4 Bathroom</span><i></i><span><svg width="14" height="13" viewBox="0 0 14 13"><path d="M7 0L0 6h2v7h4V9h2v4h4V6h2z" fill="#1c2659"/></svg>3000sqft</span></div>
  <a class="btn btn-navy">View Property</a>
</article>

<article class="prop raised" style="left:425px">
  <div class="photo" role="img" aria-label="Wood-panelled living room with large screen" style="background:linear-gradient(180deg,#6b513a,#b29274 50%,#d8cbbb)"></div>
  <span class="tag">For Sale</span>
  <h3>Luxury Villa Property</h3>
  <div class="loc"><svg width="10" height="13" viewBox="0 0 10 13"><path d="M5 0a5 5 0 0 0-5 5c0 3.5 5 8 5 8s5-4.5 5-8a5 5 0 0 0-5-5zm0 7a2 2 0 1 1 0-4 2 2 0 0 1 0 4z" fill="#1c2659"/></svg>Dominican Republic</div>
  <div class="desc">It Has Survived Not Only Five Centuries, But Also The Leap Into Sed Electronic Typesetting, Remaining.</div>
  <div class="feats"><span><svg width="18" height="11" viewBox="0 0 18 11"><path d="M1 0v11M1 7h16v4M4 4h13v3" stroke="#1c2659" stroke-width="1.6" fill="none"/></svg>6 BED</span><i></i><span><svg width="14" height="13" viewBox="0 0 14 13"><path d="M1 6h12v3a3 3 0 0 1-3 3H4a3 3 0 0 1-3-3zM3 6V1h3" stroke="#1c2659" stroke-width="1.5" fill="none"/></svg>3 Bathroom</span><i></i><span><svg width="14" height="13" viewBox="0 0 14 13"><path d="M7 0L0 6h2v7h4V9h2v4h4V6h2z" fill="#1c2659"/></svg>2500sqft</span></div>
  <a class="btn btn-gold">View Property</a>
</article>

<article class="prop" style="left:792px">
  <div class="photo" role="img" aria-label="Villa with lit pool at twilight" style="background:linear-gradient(180deg,#3d6fb0,#8aa7c6 45%,#c9a57a 70%,#3d7aa8)"></div>
  <span class="tag">For Sale</span>
  <h3>Luxury Villa Property</h3>
  <div class="loc"><svg width="10" height="13" viewBox="0 0 10 13"><path d="M5 0a5 5 0 0 0-5 5c0 3.5 5 8 5 8s5-4.5 5-8a5 5 0 0 0-5-5zm0 7a2 2 0 1 1 0-4 2 2 0 0 1 0 4z" fill="#1c2659"/></svg>Dominican Republic</div>
  <div class="desc">It Has Survived Not Only Five Centuries, But Also The Leap Into Sed Electronic Typesetting, Remaining.</div>
  <div class="feats"><span><svg width="18" height="11" viewBox="0 0 18 11"><path d="M1 0v11M1 7h16v4M4 4h13v3" stroke="#1c2659" stroke-width="1.6" fill="none"/></svg>8 BED</span><i></i><span><svg width="14" height="13" viewBox="0 0 14 13"><path d="M1 6h12v3a3 3 0 0 1-3 3H4a3 3 0 0 1-3-3zM3 6V1h3" stroke="#1c2659" stroke-width="1.5" fill="none"/></svg>4 Bathroom</span><i></i><span><svg width="14" height="13" viewBox="0 0 14 13"><path d="M7 0L0 6h2v7h4V9h2v4h4V6h2z" fill="#1c2659"/></svg>3000sqft</span></div>
  <a class="btn btn-navy">View Property</a>
</article>
<div class="dots" style="top:2022px"><span></span><span class="on"></span><span></span><span></span></div>

<section class="facilities" role="img" aria-label="Twilight coastline backdrop">
  <div class="eyebrow">Why Choose Us</div>
  <h2 class="section-title">Our Property Facilities</h2>
  <svg class="arrow" style="left:22px;top:292px" viewBox="0 0 22 32"><path d="M16 4L6 16l10 12" stroke="#fff" stroke-width="2" fill="none"/></svg>
  <svg class="arrow" style="left:1156px;top:292px" viewBox="0 0 22 32"><path d="M6 4l10 12L6 28" stroke="#fff" stroke-width="2" fill="none"/></svg>
  <div class="fac" style="left:61px"><div class="ico" role="img" aria-label="Wi-Fi router illustration"></div><h4>Wi-Fi Internet</h4><p>Lorem Ipsum Is Simply Dummy Text Of The Printing And Typesetting...</p></div>
  <div class="fac" style="left:334px"><div class="ico" role="img" aria-label="Interior furniture illustration"></div><h4>Luxury Interiors</h4><p>Lorem Ipsum Is Simply Dummy Text Of The Printing And Typesetting...</p></div>
  <div class="fac" style="left:610px"><div class="ico" role="img" aria-label="Concierge service illustration"></div><h4>Personalized Service</h4><p>Lorem Ipsum Is Simply Dummy Text Of The Printing And Typesetting...</p></div>
  <div class="fac" style="left:883px"><div class="ico" role="img" aria-label="Window view illustration"></div><h4>Unmatched Views</h4><p>Lorem Ipsum Is Simply Dummy Text Of The Printing And Typesetting...</p></div>
</section>

<div class="eyebrow" style="top:2711px">Gallery</div>
<h2 class="section-title" style="top:2746px">Our Photo Gallery</h2>
<svg class="arrow" style="left:22px;top:3001px" viewBox="0 0 22 32"><path d="M16 4L6 16l10 12" stroke="#1c2659" stroke-width="2" fill="none"/></svg>
<svg class="arrow" style="left:1156px;top:3001px" viewBox="0 0 22 32"><path d="M6 4l10 12L6 28" stroke="#1c2659" stroke-width="2" fill="none"/></svg>
<div class="photo" role="img" aria-label="Villa facade with infinity pool at dusk" style="left:61px;top:2842px;width:280px;height:349px;background:linear-gradient(180deg,#3a5f8e,#7e8ea0 40%,#a98a64 65%,#2f6d96)"></div>
<div class="photo" role="img" aria-label="Spacious bedroom opening onto garden" style="left:358px;top:2842px;width:484px;height:349px;background:linear-gradient(180deg,#5d4a3a,#a08b76 40%,#c9b8a2 70%,#8a735c)"></div>
<div class="photo" role="img" aria-label="Modern villa on a green lawn" style="left:858px;top:2842px;width:281px;height:349px;background:linear-gradient(180deg,#86b0d8,#c9c6bd 45%,#6e9a55 80%,#4d7a39)"></div>

<div class="eyebrow" style="top:3276px">Testimonials</div>
<h2 class="section-title" style="top:3311px">What Our Clients Says</h2>
<div class="testi" style="left:61px"><div class="stars">★★★★★</div><p>“Lorem Ipsum Is Simply Dummy Text Of The Printing And Typesetting Industry. Lorem Ipsum Has Been The Industry's Standard Dummy Text Ever Since The 1500s, When An Unknown Printer Took A Galley.”</p><div class="face" role="img" aria-label="Portrait of Clara Wentworth"></div><h5>Clara Wentworth</h5><div class="date">August 2025</div><div class="quote">”</div></div>
<div class="testi" style="left:425px"><div class="stars">★★★★★</div><p>“Lorem Ipsum Is Simply Dummy Text Of The Printing And Typesetting Industry. Lorem Ipsum Has Been The Industry's Standard Dummy Text Ever Since The 1500s, When An Unknown Printer Took A Galley.”</p><div class="face" role="img" aria-label="Portrait of Ravi Holloway"></div><h5>Ravi Holloway</h5><div class="date">August 2025</div><div class="quote">”</div></div>
<div class="testi" style="left:792px"><div class="stars">★★★★★</div><p>“Lorem Ipsum Is Simply Dummy Text Of The Printing And Typesetting Industry. Lorem Ipsum Has Been The Industry's Standard Dummy Text Ever Since The 1500s, When An Unknown Printer Took A Galley.”</p><div class="face" role="img" aria-label="Portrait of Tomas Edevane"></div><h5>Tomas Edevane</h5><div class="date">August 2025</div><div class="quote">”</div></div>
<div class="dots" style="top:3828px"><span></span><span class="on"></span><span></span><span></span></div>

<footer class="dark">
  <h2>Sign Up For Exclusive Updates!</h2>
  <div class="lead">“Lorem Ipsum Is Simply Dummy Text Of The Printing And Typesetting Industry. Lorem Ipsum Has Been The Industry's Standard Dummy Text Ever Since The 1500s.</div>
  <div class="signup"><span>Enter Your Email...</span><a class="btn btn-gold">Subscribe Now</a></div>

  <div class="foot-brand">Casa Coralina</div>
  <div class="foot-about">Lorem Ipsum is simply dummy text of the printing and typesetting industry. Lorem Ipsum has been the  when an unknown printer took a galley of type and scrambled</div>
  <div class="socials"><span></span><span></span><span></span><span></span></div>

  <div class="abs col" style="left:434px;top:373px"><h6>Quick Links</h6><ul><li>›&nbsp; Home</li><li>›&nbsp; About Us</li><li>›&nbsp; Property</li><li>›&nbsp; Photo Gallery</li><li>›&nbsp; Contact Us</li></ul></div>
  <div class="abs col contact" style="left:617px;top:373px"><h6>Get In Touch</h6><ul>
    <li><svg width="11" height="14" viewBox="0 0 10 13"><path d="M5 .8a4.2 4.2 0 0 0-4.2 4.2c0 3 4.2 7 4.2 7s4.2-4 4.2-7A4.2 4.2 0 0 0 5 .8z" stroke="#fff" fill="none"/></svg>Lorem Ipsum Dolor, 1234</li>
    <li><svg width="13" height="10" viewBox="0 0 13 10"><rect x=".5" y=".5" width="12" height="9" stroke="#fff" fill="none"/><path d="M.5.5l6 5 6-5" stroke="#fff" fill="none"/></svg>info@casacoralina.example</li>
    <li><svg width="13" height="13" viewBox="0 0 13 13"><path d="M3 1l2 3-1.3 1.3a7 7 0 0 0 4 4L9 8l3 2-1 2C6 12 1 7 1 2z" stroke="#fff" fill="none"/></svg>1234-567-890</li></ul></div>
  <div class="abs col" style="left:919px;top:373px"><h6>Photo Gallery</h6></div>
  <div class="thumb" role="img" aria-label="Pool courtyard" style="left:919px;top:414px;background:linear-gradient(180deg,#7b6a52,#b7a58a 60%,#5a9a9d)"></div>
  <div class="thumb" role="img" aria-label="Villa and pool" style="left:1033px;top:414px;background:linear-gradient(180deg,#7ea7d6,#c9c3b4 55%,#5c8d52)"></div>
  <div class="thumb" role="img" aria-label="Villa at dusk" style="left:919px;top:493px;background:linear-gradient(180deg,#2e5a8d,#a48a67 60%,#2f6d96)"></div>
  <div class="thumb" role="img" aria-label="Terrace lounge" style="left:1033px;top:493px;background:linear-gradient(180deg,#5d4a3a,#b09a80 60%,#4e8aa0)"></div>

  <div class="rule"></div>
  <div class="copy">© 2025 casacoralina.example. All Rights Reserved</div>
</footer>

</body>
</html>
```